Create a Brochure Design for Harlow Senior Living

Harlow Senior Living is a subsidiary of the Harlow Care Group. This brochure is specifically for the Harlow Senior Living company and brand. Create a 3 panel, front and back, tri-fold brochure. This brochure will be a way to introduce our senior living care home to the community, prospective, clients, and various referral partners. It is modern and state of the art home. Like the home, the brochure must be eye catching, unique in its deliverables (as it doesn’t feel like a care facility) and demonstrate both attention to detail and comfort. Our organization is sophisticated and built around warmth, care and individualized personal attention. The most important aspect of this design is to focus on creating a nurturing, warm, and inviting feel where you would want to put your own loved ones in our care home.
I am open to the creativity of the designer to develop something based on the above criteria; however I would like the design to work well with the existing collateral material. What I mean by that is that while I want everything to have its own personality and stand out as its own brand representative, I still need to be able to tell that the overall design concept stays stylistically inside of the same ‘family’ of existing designed material. Because of this, below I would like for the designer to pull inspiration from the link to our website (Located below) as well as from the attachment of our recently refreshed business cards (Attached). This should allow each design to be unique and creative, while still staying inside of a framework and the feel/style that I am looking for.
Finally, I want all the designers to understand that this brochure design is for a facility where we are responsible to provide care for active, positive, and happy seniors/elders. We have care professionals and staff on-site to provide 24x7, around the clock, care to the elders and geriatric residents as it is needed and required. The photos that are used must represent aging gracefully and with elegance.
Target Market(s)
Seniors(50+), Caring Family Members, Social Workers, Physicians, Hospitals
Industry/Entity Type
Business
Requirements
Must have
- • The company logo must be included.
Nice to have
- Attached you will find a sampling of images related to the long term care industry. Please feel free to use your own images as you see fit. The interior care home pictures are of our actual facility and should be incorporated into the brochure and your design.
Company Information
• Look under the Harlow Senior Living tab at
www.harlowcaregroup.example.

```html
<!DOCTYPE html>
<html lang="en">
<head>
<meta charset="utf-8">
<title>Harlow Senior Living – Brochure</title>
<link rel="stylesheet" href="https://fonts.googleapis.com/css2?family=Crimson+Text:ital@0;1&family=Gentium+Book+Plus&display=swap">
<style>
  :root {
    --backdrop: #e9e9e9;
    --paper: #ffffff;
    --paper-fold: #ececec;
    --teal: #4f918c;
    --teal-deep: #3f807b;
    --teal-light: #62a39d;
    --ink: #3b3b3b;
    --on-teal: #ffffff;
  }
  * { box-sizing: border-box; margin: 0; padding: 0; }
  html, body { width: 1200px; height: 600px; overflow: hidden; background: var(--backdrop); }
  body { position: relative; font-family: "Gentium Book Plus", Georgia, serif; color: var(--ink); }

  .brochure {
    position: absolute; left: 36px; top: 33px; width: 1122px; height: 528px;
    display: flex;
  }
  .panel { position: relative; width: 374px; height: 100%; }
  .panel--intro { background: linear-gradient(90deg, var(--paper) 0%, var(--paper) 78%, var(--paper-fold) 100%); }
  .panel--purpose { background: linear-gradient(90deg, var(--paper-fold) 0%, var(--paper) 22%, var(--paper) 100%); }
  .panel--home { background: linear-gradient(180deg, var(--teal-light) 0%, var(--teal) 45%, var(--teal-deep) 100%); }

  .photo { position: absolute; }
  .photo--carer { left: 17px; top: 17px; width: 340px; height: 250px; background: linear-gradient(120deg, #8fc3d8 0%, #e8e4df 45%, #f3efe9 100%); }
  .photo--coast { left: 15px; top: 17px; width: 339px; height: 249px; background: linear-gradient(180deg, #b9d4ea 0%, #d7e6f0 38%, #8e8070 62%, #a08c72 100%); }
  .photo--lounge { left: 17px; top: 17px; width: 340px; height: 212px; background: linear-gradient(160deg, #e4d3a4 0%, #a98a62 45%, #8d7a68 75%, #b9ad9b 100%); }
  .photo--bath { left: 160px; top: 247px; width: 197px; height: 120px; background: linear-gradient(120deg, #e5ded0 0%, #d9cfbe 55%, #b6763f 100%); }

  .brand {
    position: absolute; display: flex; align-items: center; gap: 5px;
    font-family: "Crimson Text", Georgia, serif; font-size: 14px; color: var(--teal); line-height: 1;
    white-space: nowrap;
  }
  .brand__mark { width: 11px; height: 11px; background: var(--teal); flex: none; }
  .brand--intro { right: 26px; top: 240px; }
  .brand--purpose { left: 28px; top: 60px; }

  .headline {
    position: absolute; font-family: "Crimson Text", Georgia, serif; font-weight: 400;
    font-size: 32px; line-height: 1; color: var(--teal); white-space: nowrap;
  }
  .headline--intro { left: 156px; top: 280px; }
  .headline--purpose { right: 12px; top: 280px; }

  .body-copy { position: absolute; font-size: 8.3px; line-height: 9.9px; }
  .body-copy p + p { margin-top: 9.9px; }
  .body-copy--intro { left: 156px; top: 329px; width: 198px; }
  .body-copy--purpose { left: 152px; top: 329px; width: 198px; }

  .pull-quote {
    position: absolute; display: flex; align-items: center; gap: 3px;
    font-family: "Crimson Text", Georgia, serif; font-style: italic; color: var(--teal);
  }
  .pull-quote__brace {
    display: inline-block; width: 12px; overflow: visible; text-align: center;
    font-style: normal; font-size: 60px; line-height: 1; font-weight: 400;
    transform: scaleX(0.5);
  }
  .pull-quote__text { font-size: 9px; line-height: 10.4px; width: 108px; }
  .pull-quote--intro { left: 12px; top: 284px; }
  .pull-quote--purpose { left: 12px; top: 432px; }

  .fees { position: absolute; left: 24px; top: 376px; color: var(--on-teal); font-size: 8.6px; line-height: 10.2px; }
  .fees__title { margin-bottom: 10px; }
  .fees__list { list-style: none; }

  .home-copy { position: absolute; left: 159px; top: 388px; width: 200px; color: var(--on-teal); font-size: 8.6px; line-height: 10.2px; }
  .home-copy p + p { margin-top: 10px; }
</style>
</head>
<body>
<main class="brochure">
  <section class="panel panel--intro">
    <div class="photo photo--carer" role="img" aria-label="Nurse in blue scrubs with her arm around a smiling elderly woman"></div>
    <div class="brand brand--intro"><span class="brand__mark"></span>Harlow Senior Living</div>
    <div class="pull-quote pull-quote--intro">
      <span class="pull-quote__brace">{</span>
      <span class="pull-quote__text">Neighbours live at our home. Not residents, not patient - we are all neigbours. We are family.</span>
      <span class="pull-quote__brace">}</span>
    </div>
    <h2 class="headline headline--intro">We are family.</h2>
    <div class="body-copy body-copy--intro">
      <p>Harlow Senior Living is a unique care concept, designed around a social model which encourages “neighbors” to be as independent as possible, actively participate in life here, and interact with their fellow neighbors.</p>
      <p>Harlow Care Group is proud to usher in a new era in long-term care - Harlow Senior Living. Harlow Senior Living was developed as a response to innumerable requests from our clients for assistance locating suitable homes or facilities when in-home care is no longer appropriate. Now, your care can remain with the best!</p>
      <p>Stay busy doing what you love here! Participate in as many activities as you like and discover life anew. Keep up your favorite hobbies or take up new ones.</p>
    </div>
  </section>

  <section class="panel panel--purpose">
    <div class="photo photo--coast" role="img" aria-label="Senior man in a wheelchair and his wife pointing out to sea from a seaside boardwalk"></div>
    <div class="brand brand--purpose"><span class="brand__mark"></span>Harlow Senior Living</div>
    <h2 class="headline headline--purpose">Life has a purpose.</h2>
    <div class="body-copy body-copy--purpose">
      <p>Here, you’ll maintain purpose in life while having personal care assistance as needed, activities, exercise, transportation, and companionship. Professional staff will be in residence 24 hours a day. This is a very special home, offering you a loving and nurturing life experience.</p>
      <p>In our home, neighbors can do gardening, stay in touch with family and friends on Friendlink, email, or by CallNest, relax in the soaking tub, take up a new hobby, enjoy music and crafts, community outings, exercise programs, beach walks, movie nights, board games, barbecues, and a whole lot more.</p>
      <p>Harlow Senior Living is a home where neighbors are actively engaged, individuality is encouraged, and life has purpose. It’s a home!</p>
    </div>
    <div class="pull-quote pull-quote--purpose">
      <span class="pull-quote__brace">{</span>
      <span class="pull-quote__text">Neighbours are actively engaged, individuality is encouraged and life has a purpose.</span>
      <span class="pull-quote__brace">}</span>
    </div>
  </section>

  <section class="panel panel--home">
    <div class="photo photo--lounge" role="img" aria-label="Bright family room with sectional sofa, kitchen and dining area"></div>
    <div class="photo photo--bath" role="img" aria-label="Accessible private bathroom with shower, grab bars and vanity"></div>
    <div class="fees">
      <p class="fees__title">Monthly Fees Include</p>
      <ul class="fees__list">
        <li>3 daily meals + snacks</li>
        <li>Activities</li>
        <li>Laundry</li>
        <li>Housekeeping</li>
        <li>Utilities</li>
        <li>Accommodations</li>
        <li>Medication Management</li>
        <li>Care Planning</li>
        <li>Regular Nursing Visits</li>
        <li>Access to Staff 24/7</li>
      </ul>
    </div>
    <div class="home-copy">
      <p>The home features areas for activities &amp; relaxation, with 2 large family rooms, a dining room, a kitchen, a spa room with soaking tub and hair washing sink.</p>
      <p>Up to 22 “neighbors” enjoy this 11,000 square feet home with 19 fully-furnished private rooms with private bathrooms. Room sizes range from 152 sq ft to 225 sq ft. Each has a flat screen television, electric bed(s), desk, chair, dressers, art work, built-in closet system with mirrored doors, independent air conditioner, and ceiling fan.</p>
    </div>
  </section>
</main>
</body>
</html>
```